Social Media Graphics - Harbor Climb REVISED

Create 6-7 individual social media graphics (square size) to encourage folks to join our online course called:

The Lantern Ledger Plan
How to Launch a Multi-Million Business From Scratch
Sign Up Today!

IMPORTANT: Make the largest and most prominent text on the graphic be: How to Launch a Multi-Million Business From Scratch

For the color scheme of the graphics, let's try a blue color palette; make sure the graphics appeal to both men and women

Make sure each graphic contains 1 of the 3 pics attached (crop pic as needed); and make sure one of the graphics is all TEXT only.

Target Market(s)

men and women looking to start a business

Industry/Entity Type

Entrepreneurship

Colors
0054AA
0677BA
7BADD7
CADEEF
E8F1F8

Requirements
Must have
• All the text and use the 3 pics provided; one graphic can be all text; Simple, modern design that's easy to read

```html
<!DOCTYPE html>
<html lang="en">
<head>
<meta charset="UTF-8">
<title>The Lantern Ledger Plan – Social Graphic</title>
<link href="https://fonts.googleapis.com/css2?family=Poppins:wght@200;400;700;800&display=swap" rel="stylesheet">
<style>
  :root {
    --navy: #00317f;
    --white: #ffffff;
    --photo-warm-1: #efe3d4;
    --photo-warm-2: #b9a08a;
    --photo-warm-3: #5a4a44;
    --portrait-dark-1: #2c2f3a;
    --portrait-dark-2: #8c5a4a;
    --portrait-pink-1: #f6c9d3;
    --portrait-pink-2: #d8315b;
    --swoosh-grey: #e3e4e6;
  }
  html, body {
    margin: 0;
    padding: 0;
    width: 1200px;
    height: 1200px;
    overflow: hidden;
    background: var(--white);
  }
  .graphic {
    position: relative;
    width: 1200px;
    height: 1200px;
    background: var(--white);
    font-family: "Poppins", sans-serif;
    color: var(--navy);
    overflow: hidden;
  }
  .backdrop {
    position: absolute;
    inset: 0;
  }
  .portrait {
    position: absolute;
    border-radius: 50%;
    border: 5px solid var(--navy);
    box-sizing: border-box;
  }
  .portrait--small {
    left: 573px;
    top: 423px;
    width: 258px;
    height: 258px;
    background: linear-gradient(160deg, #e9e4e0 0%, var(--portrait-dark-2) 45%, var(--portrait-dark-1) 100%);
  }
  .portrait--large {
    left: 808px;
    top: 323px;
    width: 354px;
    height: 354px;
    background: linear-gradient(160deg, var(--portrait-pink-1) 0%, var(--portrait-pink-2) 55%, var(--portrait-dark-1) 100%);
  }
  .course-name {
    position: absolute;
    top: 708px;
    left: 0;
    right: 0;
    margin: 0;
    text-align: center;
    font-size: 50px;
    font-weight: 700;
    letter-spacing: 1px;
    line-height: 1;
    white-space: nowrap;
  }
  .course-name__lead {
    font-weight: 200;
  }
  .headline {
    position: absolute;
    top: 784px;
    left: 60px;
    right: 60px;
    margin: 0;
    text-align: center;
    font-size: 70px;
    font-weight: 800;
    line-height: 1.08;
    letter-spacing: -0.5px;
  }
  .headline__line {
    display: block;
    white-space: nowrap;
  }
  .cta-band {
    position: absolute;
    left: 0;
    bottom: 0;
    width: 1200px;
    height: 120px;
  }
  .cta-label {
    position: absolute;
    left: 0;
    right: 0;
    top: 1122px;
    margin: 0;
    text-align: center;
    color: var(--white);
    font-size: 46px;
    font-weight: 700;
    line-height: 1;
  }
</style>
</head>
<body>
  <main class="graphic">
    <svg class="backdrop" width="1200" height="1200" viewBox="0 0 1200 1200">
      <defs>
        <linearGradient id="photoTone" x1="0" y1="0" x2="1" y2="1">
          <stop offset="0" stop-color="var(--photo-warm-1)"/>
          <stop offset="0.55" stop-color="var(--photo-warm-2)"/>
          <stop offset="1" stop-color="var(--photo-warm-3)"/>
        </linearGradient>
        <linearGradient id="swooshShade" x1="0" y1="0" x2="1" y2="0">
          <stop offset="0" stop-color="var(--swoosh-grey)" stop-opacity="0"/>
          <stop offset="0.6" stop-color="var(--swoosh-grey)"/>
          <stop offset="1" stop-color="var(--swoosh-grey)" stop-opacity="0"/>
        </linearGradient>
      </defs>
      <path class="hero-photo" role="img" aria-label="Photo of the two course hosts speaking on stage with a microphone"
            d="M0 0 H1200 V420 C1000 500 800 560 580 565 C330 570 130 500 0 405 Z"
            fill="url(#photoTone)"/>
      <path class="swoosh-shade" d="M40 470 C200 560 420 610 560 612 C420 625 220 600 40 470 Z" fill="url(#swooshShade)"/>
      <path class="swoosh-line" d="M0 410 C140 510 340 580 580 578 C800 576 1000 515 1200 440"
            fill="none" stroke="var(--navy)" stroke-width="9"/>
      <path class="swoosh-band" d="M1000 500 C1080 470 1140 445 1200 420 V462 C1140 485 1080 505 1020 520 Z" fill="var(--navy)"/>
      <path class="cta-band" d="M142 1200 C380 1060 820 1060 1075 1200 Z" fill="var(--navy)"/>
    </svg>

    <div class="portrait portrait--small" role="img" aria-label="Portrait of the two hosts standing with arms crossed in dark outfits"></div>
    <div class="portrait portrait--large" role="img" aria-label="Portrait of the two hosts smiling against a pink backdrop"></div>

    <p class="course-name"><span class="course-name__lead">THE</span> LANTERN LEDGER PLAN</p>
    <h1 class="headline">
      <span class="headline__line">How to Launch a</span>
      <span class="headline__line">Multi-Million Business</span>
      <span class="headline__line">From Scratch</span>
    </h1>
    <p class="cta-label">Sign Up Today!</p>
  </main>
</body>
</html>
```